Business cards for a tribute and obituary website

Our website is called Quiet Orchard.

It is a special place online for people to remember their loved ones who have passed away, through obituaries and tributes. Friends and family can also convey their condolences on the deceased's memorial page. Celebrating the life of the deceased and remembering their legacy is very important to us – death should not be just about grieving.

We would like the card to look tasteful and modern. The design should ideally not have colours that are too bright. The logo and website URL, www.quietorchardpages.net should be visible on the front of the card, with our slogan "Celebrating a life passed" on the back.

The design should communicate our purpose – remembering loved ones who have passed – and also a lighter tone of celebrating life. It should not look like a funeral director's card!

Our logo has been attached. Looking forward to some beautiful designs! Get creative :)
Updates

Reason: Thank you all for your designs. The rest of my team and I have not reached a decision on which design to select and I am collecting feedback from them. I will provide feedback for any changes that need to be made soon. It would be great if we could see more original designs and in more colours! We will definitely select a design by this deadline.

Industry/Entity Type

Business

Contact Information for Business Card

Nadia Fenwick
Project Manager
471226809
nadiafenwick@quietorchardpages.net

Font styles to use
Serif
Sans Serif

Requirements
Must have
• Logo and website address (www.quietorchardpages.net) on the front.
Nice to have
• Hi designers! It would be nice to see alternative colours – feel free to try out colours that are tasteful and subtle. The colour of the business card does not have to be the same as the logo.
• We would also like to see the logo used in different ways, perhaps a glossy or embossed finish. The card should look stylish.

```html
<!DOCTYPE html>
<html lang="en">
<head>
<meta charset="utf-8">
<title>Quiet Orchard – Business Card</title>
<link rel="stylesheet" href="https://fonts.googleapis.com/css2?family=Roboto+Slab:wght@700&family=Exo+2:wght@400;500&display=swap">
<style>
  :root {
    --page: #dfe2e5;
    --card-grey: #9b9c9e;
    --card-grey-light: #b4b5b7;
    --navy: #0a2a4f;
    --swoosh: #f1f2f3;
    --white: #ffffff;
    --name-ink: #f4f4f4;
  }
  * { margin: 0; padding: 0; box-sizing: border-box; }
  html, body {
    width: 1200px; height: 864px; overflow: hidden;
    background: var(--page);
  }
  .canvas {
    position: relative; width: 1200px; height: 864px;
    display: flex; align-items: center; justify-content: center;
  }
  .card {
    position: relative; width: 1050px; height: 600px;
    background: linear-gradient(160deg, var(--card-grey) 0%, var(--card-grey) 55%, var(--card-grey-light) 100%);
    box-shadow: 0 10px 30px rgba(0,0,0,0.18);
    overflow: hidden;
  }
  .card-shapes { position: absolute; inset: 0; }

  .brand {
    position: absolute; left: 585px; top: 48px;
    display: flex; align-items: center; gap: 22px;
  }
  .brand-dot {
    width: 74px; height: 74px; border-radius: 50%;
    background: var(--white);
  }
  .brand-name {
    font-family: "Roboto Slab", serif; font-weight: 700;
    font-size: 56px; line-height: 0.95; color: var(--white);
  }

  .contact {
    position: absolute; right: 40px; top: 192px;
    list-style: none; text-align: right;
    font-family: "Exo 2", sans-serif; font-weight: 400;
    color: var(--white); font-size: 18px; letter-spacing: 0.5px;
  }
  .contact li {
    display: flex; justify-content: flex-end; align-items: center;
    gap: 12px; line-height: 1.25; margin-bottom: 10px;
  }
  .contact .address { font-size: 20px; margin-bottom: 18px; }
  .contact .address span { display: block; }
  .contact .plain { font-size: 16px; margin-bottom: 6px; }
  .contact svg { width: 19px; height: 19px; flex: none; }

  .person {
    position: absolute; left: 78px; bottom: 62px;
    font-family: "Exo 2", sans-serif; color: var(--name-ink);
  }
  .person-name { font-size: 31px; font-weight: 500; letter-spacing: 1.5px; text-transform: uppercase; }
  .person-role { font-size: 22px; font-weight: 400; letter-spacing: 1px; margin-top: 2px; padding-left: 30px; }
</style>
</head>
<body>
<main class="canvas">
  <article class="card">
    <svg class="card-shapes" viewBox="0 0 1050 600" width="1050" height="600" aria-hidden="true">
      <path class="swoosh" fill="var(--swoosh)"
        d="M 450 0 H 520 C 420 80 330 200 360 310 C 390 410 480 462 590 482 C 430 474 300 410 280 300 C 262 190 340 80 450 0 Z"/>
      <path class="navy-field" fill="var(--navy)"
        d="M 500 0 H 1050 V 482 C 900 502 720 500 600 482 C 440 458 350 385 345 285 C 340 175 410 70 500 0 Z"/>
      <path fill="none" stroke="var(--navy)" stroke-width="3"
        d="M 290 285 C 300 400 440 474 600 488"/>
    </svg>

    <div class="brand">
      <span class="brand-dot"></span>
      <span class="brand-name">Quiet<br>Orchard</span>
    </div>

    <ul class="contact">
      <li class="address"><div><span>12 Linden Row, Floor 4</span><span>Ashby Lane</span></div></li>
      <li>471 226 809
        <svg viewBox="0 0 24 24" fill="var(--white)"><path d="M6.6 10.8a15 15 0 0 0 6.6 6.6l2.2-2.2c.3-.3.7-.4 1-.2 1.1.4 2.3.6 3.6.6.6 0 1 .4 1 1V20c0 .6-.4 1-1 1A17 17 0 0 1 3 4c0-.6.4-1 1-1h3.5c.6 0 1 .4 1 1 0 1.3.2 2.5.6 3.6.1.3 0 .7-.2 1z"/></svg>
      </li>
      <li>471 226 810
        <svg viewBox="0 0 24 24" fill="none" stroke="var(--white)" stroke-width="2"><rect x="6" y="2" width="12" height="20" rx="2"/><line x1="10" y1="18" x2="14" y2="18"/></svg>
      </li>
      <li>471 226 811
        <svg viewBox="0 0 24 24" fill="var(--white)"><rect x="3" y="9" width="18" height="12" rx="1"/><rect x="7" y="3" width="10" height="5" fill="none" stroke="var(--white)" stroke-width="2"/></svg>
      </li>
      <li>info@quietorchardpages.net
        <svg viewBox="0 0 24 24" fill="none" stroke="var(--white)" stroke-width="2"><rect x="2" y="5" width="20" height="14"/><path d="M2 5l10 8 10-8"/></svg>
      </li>
      <li class="plain">nadiafenwick@quietorchardpages.net</li>
      <li class="plain">www.quietorchardpages.net
        <svg viewBox="0 0 24 24" fill="none" stroke="var(--white)" stroke-width="2"><circle cx="12" cy="12" r="10"/><ellipse cx="12" cy="12" rx="4" ry="10"/><line x1="2" y1="12" x2="22" y2="12"/></svg>
      </li>
    </ul>

    <div class="person">
      <p class="person-name">Nadia Fenwick</p>
      <p class="person-role">Project Manager</p>
    </div>
  </article>
</main>
</body>
</html>
```